Media Training Presentation (template)

This is a 49-slide power point deck to be used in training clients to deal with the media in various settings. We need a template we can personalize for different clients. The overall color scheme should match our logo. It should look very professional, but also engaging. The word doc contains all of the text, images, and videos for each slide. Also uploaded our logo. Please match/coordinate colors of presentation to the logo colors. If you prefer, you can submit five or six slides showing the overall design and a template for each type of slide, then complete the remainder of the slides within 24 hours if chosen. (Sorry for the quick turnaround…we didn’t know we would need it this quickly!) Thanks for submitting!
Target Market(s)
Government and corporate clients

```html
<!DOCTYPE html>
<html lang="en">
<head>
<meta charset="utf-8">
<title>Media Training Presentation – Slide Templates</title>
<link href="https://fonts.googleapis.com/css2?family=Outfit:wght@500;600;700&family=Hind:wght@400;500&display=swap" rel="stylesheet">
<style>
  :root{
    --brand:#0b4fae;
    --brand-dark:#083f8c;
    --ink:#1f1f24;
    --muted:#3b3b44;
    --paper:#ffffff;
    --canvas:#ffffff;
    --line:#cfd6e2;
  }
  *{box-sizing:border-box;margin:0;padding:0}
  html,body{width:1200px;height:1111px;overflow:hidden;background:var(--canvas)}
  body{position:relative;font-family:"Hind",sans-serif;color:var(--ink)}
  .sprite{position:absolute;width:0;height:0;overflow:hidden}

  .slide{position:absolute;width:509px;height:286px;background:var(--paper);
    box-shadow:0 4px 14px rgba(0,0,0,.12);overflow:hidden}
  .slide--intro{left:70px;top:77px}
  .slide--video{left:619px;top:77px}
  .slide--goals{left:70px;top:408px}
  .slide--negotiate{left:619px;top:412px}
  .slide--story{left:70px;top:739px}
  .slide--record{left:619px;top:739px}

  .top-band{position:absolute;left:0;top:0;width:439px;height:17px;background:var(--brand)}
  .brand{position:absolute;left:444px;top:3px;display:flex;align-items:center;gap:4px}
  .brand__square{width:9px;height:9px;border:1.5px solid var(--brand)}
  .brand__name{font-family:"Outfit",sans-serif;font-weight:500;font-size:8.5px;letter-spacing:.6px;color:var(--brand)}

  .footer{position:absolute;left:0;bottom:0;width:473px;height:17px;background:var(--brand);
    display:flex;align-items:center;color:#fff;font-family:"Outfit",sans-serif;font-size:6.3px;font-weight:500}
  .footer__item{display:flex;align-items:center;gap:4px}
  .footer__item--mail{margin-left:10px;width:88px}
  .footer__divider{width:1px;height:11px;background:rgba(255,255,255,.7);margin-right:14px}
  .footer svg{width:8px;height:8px;fill:none;stroke:#fff;stroke-width:1.4}
  .page-no{position:absolute;right:6px;bottom:5px;font-family:"Outfit",sans-serif;font-size:6.5px;color:var(--ink)}

  .title{position:absolute;left:0;width:100%;text-align:center;font-family:"Outfit",sans-serif;
    font-weight:600;font-size:18.5px;line-height:1.05;color:var(--ink)}
  .rule{position:absolute;height:2px;width:37px;background:var(--brand)}
  .rule--center{left:236px}

  .card{position:absolute;width:133px;height:131px;background:#fff;
    box-shadow:0 2px 8px rgba(0,0,0,.11);border-radius:3px}
  .card__icon{position:absolute;left:41px;top:28px;width:50px;height:50px}
  .card__label{position:absolute;left:4px;right:4px;top:98px;text-align:center;font-size:10.8px;line-height:1.05;color:var(--ink)}

  .icon{fill:none;stroke:var(--ink);stroke-width:1.6;stroke-linecap:round;stroke-linejoin:round}
  .icon .accent{stroke:var(--brand)}

  .media{position:absolute;border-radius:5px}
  .media--interview{left:67px;top:79px;width:376px;height:174px;
    background:radial-gradient(ellipse at 45% 45%,#8d7a66 0%,#5e5244 35%,#3b3f36 70%,#2a302b 100%)}
  .media--handshake{left:197px;top:39px;width:298px;height:211px;border:3px solid var(--brand);border-radius:3px;
    background:linear-gradient(110deg,#c9d6e6 0%,#a7b9d0 35%,#d8dde2 55%,#4f6785 80%,#2b3b55 100%)}
  .media--visit{left:34px;top:53px;width:441px;height:205px;border-radius:4px;
    background:linear-gradient(100deg,#b9858a 0%,#d8c4c0 30%,#ece6e2 50%,#9c3a44 68%,#2d3446 100%)}

  .goal-label{position:absolute;font-size:10.3px;font-weight:500;color:var(--muted);white-space:nowrap;transform:translateX(-50%)}
  .timeline{position:absolute;left:0;top:0;width:509px;height:286px}

  .agenda{position:absolute;right:334px;top:114px;list-style:none;text-align:right}
  .agenda li{font-size:10.6px;font-weight:500;color:var(--muted);line-height:18.7px;white-space:nowrap}
  .agenda li::after{content:"";display:inline-block;width:3.5px;height:3.5px;border-radius:50%;background:var(--brand);margin-left:6px;vertical-align:2px}
  .negotiate-title{position:absolute;right:332px;top:77px;font-family:"Outfit",sans-serif;font-weight:600;font-size:18px;color:var(--ink);white-space:nowrap}
</style>
</head>
<body>

<svg class="sprite" aria-hidden="true">
  <defs>
    <symbol id="gear" viewBox="0 0 30 30">
      <circle cx="15" cy="15" r="10" fill="none" stroke-width="4" stroke-dasharray="3.2 2.05"/>
      <circle cx="15" cy="15" r="8" fill="#fff" stroke-width="1.6"/>
      <circle cx="15" cy="15" r="3.5" fill="none" stroke-width="1.6"/>
    </symbol>
  </defs>
</svg>

<!-- Slide: What is media training -->
<section class="slide slide--intro">
  <div class="top-band"></div>
  <div class="brand"><span class="brand__square"></span><span class="brand__name">HARLOW</span></div>
  <h2 class="title" style="top:36px">What is media training?</h2>
  <div class="rule rule--center" style="top:60px"></div>

  <div class="card" style="left:24px;top:88px">
    <svg class="card__icon icon" viewBox="0 0 50 50">
      <use href="#gear" x="2" y="14" width="26" height="26" stroke="var(--ink)"/>
      <use href="#gear" x="22" y="6" width="22" height="22" stroke="var(--ink)"/>
      <path class="accent" d="M10 23a6 6 0 0 1 8-4M28 12a5 5 0 0 1 7 3"/>
    </svg>
    <p class="card__label">It’s not natural</p>
  </div>
  <div class="card" style="left:184px;top:88px">
    <svg class="card__icon icon" viewBox="0 0 50 50">
      <use href="#gear" x="18" y="2" width="15" height="15" stroke="var(--ink)"/>
      <use href="#gear" x="7" y="13" width="13" height="13" stroke="var(--ink)"/>
      <use href="#gear" x="31" y="13" width="13" height="13" stroke="var(--ink)"/>
      <circle class="accent" cx="25.5" cy="9.5" r="2"/>
      <path d="M4 24l3 10 8 8 4-4-6-7M46 24l-3 10-8 8-4-4 6-7"/>
    </svg>
    <p class="card__label">It requires practice</p>
  </div>
  <div class="card" style="left:344px;top:88px">
    <svg class="card__icon icon" viewBox="0 0 50 50">
      <path d="M18 46v-7c-6-3-9-9-8-16 1-9 9-15 18-14 9 1 14 8 14 15l4 7h-4v6h-6v9"/>
      <use href="#gear" x="17" y="11" width="18" height="18" stroke="var(--brand)"/>
      <path class="accent" d="M14 20a13 13 0 0 1 22-6l2-3"/>
    </svg>
    <p class="card__label">It’s about developing<br>a mindset</p>
  </div>

  <div class="footer">
    <span class="footer__item footer__item--mail"><svg viewBox="0 0 10 10"><rect x="1" y="2" width="8" height="6"/><path d="M1 2l4 3 4-3"/></svg>info@harlowcomms.com</span>
    <span class="footer__divider"></span>
    <span class="footer__item"><svg viewBox="0 0 10 10"><path d="M2 1l2 2-1 1.5c.8 1.5 1.8 2.5 3 3L7.5 6l2 2-1.5 1.5C5 9 1 5 .5 2z"/></svg>+1 555 010 0199</span>
  </div>
  <span class="page-no">Page 02</span>
</section>

<!-- Slide: Training and preparation -->
<section class="slide slide--video">
  <div class="top-band"></div>
  <div class="brand"><span class="brand__square"></span><span class="brand__name">HARLOW</span></div>
  <h2 class="title" style="top:27px;font-size:17.5px">Training and preparation are the difference between<br>success and failure</h2>
  <div class="rule rule--center" style="top:69px"></div>
  <div class="media media--interview" role="img" aria-label="Video still: close-up of a man answering questions in a television interview"></div>
  <div class="footer">
    <span class="footer__item footer__item--mail"><svg viewBox="0 0 10 10"><rect x="1" y="2" width="8" height="6"/><path d="M1 2l4 3 4-3"/></svg>info@harlowcomms.com</span>
    <span class="footer__divider"></span>
    <span class="footer__item"><svg viewBox="0 0 10 10"><path d="M2 1l2 2-1 1.5c.8 1.5 1.8 2.5 3 3L7.5 6l2 2-1.5 1.5C5 9 1 5 .5 2z"/></svg>+1 555 010 0199</span>
  </div>
  <span class="page-no">Page 03</span>
</section>

<!-- Slide: Goals -->
<section class="slide slide--goals">
  <div class="top-band"></div>
  <div class="brand"><span class="brand__square"></span><span class="brand__name">HARLOW</span></div>
  <h2 class="title" style="top:26px">Goals</h2>
  <div class="rule rule--center" style="top:50px"></div>

  <svg class="timeline" viewBox="0 0 509 286" aria-hidden="true">
    <g stroke="var(--ink)" stroke-width="1" fill="none">
      <line x1="94" y1="149" x2="185" y2="149"/>
      <line x1="191" y1="149" x2="292" y2="149"/>
      <line x1="298" y1="149" x2="389" y2="149"/>
      <!-- connectors -->
      <g stroke="#888" stroke-width=".8">
        <line x1="188" y1="134" x2="188" y2="114"/><path d="M186 116l2-3 2 3"/>
        <line x1="392" y1="134" x2="392" y2="114"/><path d="M390 116l2-3 2 3"/>
        <line x1="91" y1="163" x2="91" y2="183"/><path d="M89 181l2 3 2-3"/>
        <line x1="296" y1="163" x2="296" y2="183"/><path d="M294 181l2 3 2-3"/>
      </g>
    </g>
    <g fill="#888"><circle cx="188" cy="134" r="1.4"/><circle cx="392" cy="134" r="1.4"/><circle cx="91" cy="163" r="1.4"/><circle cx="296" cy="163" r="1.4"/></g>
    <g fill="var(--brand)"><circle cx="91" cy="149" r="4"/><circle cx="188" cy="149" r="4"/><circle cx="295" cy="149" r="4"/><circle cx="392" cy="149" r="4"/></g>

    <g class="icon" stroke-width="1.1">
      <!-- checklist -->
      <rect x="82" y="110" width="19" height="24" rx="1.5"/><rect x="87" y="108" width="9" height="4" rx="1"/>
      <path class="accent" d="M85 117h13M85 121h13M85 125h13M85 129h13"/>
      <!-- chart board -->
      <rect x="175" y="163" width="26" height="18" rx="1"/><path d="M186 181l-4 7M190 181l4 7"/>
      <path class="accent" d="M179 177v-4M183 177v-6M187 177v-3M180 170l4-3 3 2"/>
      <circle cx="193" cy="172" r="4"/><path d="M196 175l3 3"/>
      <!-- chat -->
      <rect x="286" y="110" width="21" height="15" rx="3"/><path d="M290 125l-2 4 5-4"/>
      <path class="accent" d="M290 108h19v14"/>
      <g fill="var(--ink)" stroke="none"><circle cx="292" cy="117.5" r="1"/><circle cx="296.5" cy="117.5" r="1"/><circle cx="301" cy="117.5" r="1"/></g>
    </g>
    <use href="#gear" x="377" y="163" width="30" height="30" stroke="var(--ink)"/>
    <path class="icon accent" stroke-width="1.2" d="M389 183v-5l3-4 3 4v5M390 181h4"/>
  </svg>

  <span class="goal-label" style="left:193px;top:87px">Develop a strategy</span>
  <span class="goal-label" style="left:397px;top:86px">Build a practice approach</span>
  <span class="goal-label" style="left:94px;top:198px">Learn how to prepare</span>
  <span class="goal-label" style="left:297px;top:197px">Clarify message</span>

  <div class="footer">
    <span class="footer__item footer__item--mail"><svg viewBox="0 0 10 10"><rect x="1" y="2" width="8" height="6"/><path d="M1 2l4 3 4-3"/></svg>info@harlowcomms.com</span>
    <span class="footer__divider"></span>
    <span class="footer__item"><svg viewBox="0 0 10 10"><path d="M2 1l2 2-1 1.5c.8 1.5 1.8 2.5 3 3L7.5 6l2 2-1.5 1.5C5 9 1 5 .5 2z"/></svg>+1 555 010 0199</span>
  </div>
  <span class="page-no">Page 04</span>
</section>

<!-- Slide: What to negotiate -->
<section class="slide slide--negotiate">
  <div class="top-band"></div>
  <div class="brand"><span class="brand__square"></span><span class="brand__name">HARLOW</span></div>
  <h2 class="negotiate-title">What to negotiate?</h2>
  <div class="rule" style="left:140px;top:101px"></div>
  <ul class="agenda">
    <li>Timing and location</li>
    <li>Rules of recording/broadcast</li>
    <li>Rules of translation</li>
    <li>Questions</li>
    <li>Recording (for accuracy)</li>
  </ul>
  <div class="media media--handshake" role="img" aria-label="Photo: a businesswoman and businessman shaking hands beside a camera on a tripod"></div>
  <div class="footer">
    <span class="footer__item footer__item--mail"><svg viewBox="0 0 10 10"><rect x="1" y="2" width="8" height="6"/><path d="M1 2l4 3 4-3"/></svg>info@harlowcomms.com</span>
    <span class="footer__divider"></span>
    <span class="footer__item"><svg viewBox="0 0 10 10"><path d="M2 1l2 2-1 1.5c.8 1.5 1.8 2.5 3 3L7.5 6l2 2-1.5 1.5C5 9 1 5 .5 2z"/></svg>+1 555 010 0199</span>
  </div>
  <span class="page-no">Page 05</span>
</section>

<!-- Slide: Create your story -->
<section class="slide slide--story">
  <div class="top-band"></div>
  <div class="brand"><span class="brand__square"></span><span class="brand__name">HARLOW</span></div>
  <h2 class="title" style="top:18px">Create your story</h2>
  <div class="rule rule--center" style="top:43px"></div>
  <div class="media media--visit" role="img" aria-label="Video still: official visitors greeting a group of schoolchildren in a school hallway"></div>
  <div class="footer">
    <span class="footer__item footer__item--mail"><svg viewBox="0 0 10 10"><rect x="1" y="2" width="8" height="6"/><path d="M1 2l4 3 4-3"/></svg>info@harlowcomms.com</span>
    <span class="footer__divider"></span>
    <span class="footer__item"><svg viewBox="0 0 10 10"><path d="M2 1l2 2-1 1.5c.8 1.5 1.8 2.5 3 3L7.5 6l2 2-1.5 1.5C5 9 1 5 .5 2z"/></svg>+1 555 010 0199</span>
  </div>
  <span class="page-no">Page 06</span>
</section>

<!-- Slide: On the record -->
<section class="slide slide--record">
  <div class="top-band"></div>
  <div class="brand"><span class="brand__square"></span><span class="brand__name">HARLOW</span></div>
  <h2 class="title" style="top:36px">On the record:</h2>
  <div class="rule rule--center" style="top:59px"></div>

  <div class="card" style="left:26px;top:88px">
    <svg class="card__icon icon" viewBox="0 0 50 50" stroke-width="2.2">
      <rect x="14" y="6" width="22" height="10" rx="2"/>
      <rect x="6" y="16" width="38" height="18" rx="4"/>
      <rect x="14" y="26" width="22" height="18" rx="2" fill="#fff"/>
      <path class="accent" d="M19 33h12M19 38h9"/>
    </svg>
    <p class="card__label">Everything for print</p>
  </div>
  <div class="card" style="left:186px;top:88px">
    <svg class="card__icon icon" viewBox="0 0 50 50" stroke-width="1.8">
      <use href="#gear" x="9" y="18" width="30" height="30" stroke="var(--ink)"/>
      <circle cx="12" cy="18" r="3"/><path d="M6 27a6 6 0 0 1 12 0"/>
      <path class="accent" d="M22 27v-6h4v6M29 27v-10h4v10M36 27v-14h4v14"/>
      <path d="M24 14l8-4 6-4M38 6h3v3"/>
    </svg>
    <p class="card__label">Your name for attribution</p>
  </div>
  <div class="card" style="left:346px;top:88px">
    <svg class="card__icon icon" viewBox="0 0 50 50" stroke-width="1.8">
      <rect x="8" y="8" width="26" height="34" rx="2"/><rect x="15" y="5" width="12" height="6" rx="1.5"/>
      <path d="M13 18h16M13 24h16M13 30h10"/>
      <path class="accent" d="M13 36h8"/>
      <path d="M44 24l-14 14-4 1 1-4 14-14z"/>
    </svg>
    <p class="card__label">Always assume everything<br>is on the record</p>
  </div>

  <div class="footer">
    <span class="footer__item footer__item--mail"><svg viewBox="0 0 10 10"><rect x="1" y="2" width="8" height="6"/><path d="M1 2l4 3 4-3"/></svg>info@harlowcomms.com</span>
    <span class="footer__divider"></span>
    <span class="footer__item"><svg viewBox="0 0 10 10"><path d="M2 1l2 2-1 1.5c.8 1.5 1.8 2.5 3 3L7.5 6l2 2-1.5 1.5C5 9 1 5 .5 2z"/></svg>+1 555 010 0199</span>
  </div>
  <span class="page-no">Page 07</span>
</section>

</body>
</html>
```